Real Estate - Property Management Prospectus/Brochure

We need a prospectus made up, around 9-10 pages including the cover page pages 3 onwards can be all a similar template happy for the front cover to have lots of black. I would like it to look very classy and futuristic, high end, blacks, silvers and whites, i am specializing in managing high end rental properties. i would like to design to correspond with the logo. I need to be able to email this booklet mostly - and also be able to print and mail out as well. I would like it crisp and clean as well - not to much on a page. Please note - happy for the cover to be simple with the logo added - prefer lots of black and with the other pages - they can all be a similar layout template to make this job easier? My website is www.leasemeridian.com.au and phone is 0418 293 540 email is tparks@leasemeridian.com.au
Target Market(s)
Investors
Industry/Entity Type
Real Estate
Requirements
Should not have
- Bright greens or bold colours

```html
<!DOCTYPE html>
<html lang="en">
<head>
<meta charset="utf-8">
<title>Lease Meridian – Property Management Prospectus Cover</title>
<link href="https://fonts.googleapis.com/css2?family=Archivo+Black&family=Oswald:wght@300;400;500&family=Lato:wght@400;700&display=swap" rel="stylesheet">
<style>
  :root {
    --backdrop: #d9d9d9;
    --ink: #0b0b0b;
    --paper: #f2f2f2;
    --silver: #c4c4c4;
    --silver-dark: #8d8d8d;
    --grey-text: #9a9a9a;
    --white: #ffffff;
    --sky-top: #6f9fd8;
    --sky-low: #b9cde0;
    --city: #8a6a58;
  }
  * { margin: 0; padding: 0; box-sizing: border-box; }
  html, body { width: 1200px; height: 907px; overflow: hidden; }
  body { background: var(--backdrop); position: relative; font-family: "Lato", sans-serif; }

  .spread {
    position: absolute; left: 100px; top: 106px; width: 1000px; height: 695px;
    display: flex; box-shadow: 0 6px 24px rgba(0,0,0,.25);
  }
  .page { position: relative; width: 500px; height: 100%; overflow: hidden; }

  /* Back cover */
  .back-cover { background: var(--ink); }
  .back-cover__skyline {
    position: absolute; left: 0; top: 0; width: 100%; height: 566px;
    background: linear-gradient(180deg, #f7f7f7 0%, #e4e4e4 45%, #cfcfcf 75%, #e9e9e9 100%);
  }
  .back-cover__rule { position: absolute; left: 0; top: 566px; width: 100%; height: 6px; background: var(--silver); }
  .contact { position: absolute; left: 44px; top: 604px; color: var(--white); }
  .contact__phone { font-weight: 700; font-size: 15px; display: flex; align-items: center; gap: 6px; margin-bottom: 4px; }
  .contact__line { font-size: 12px; display: flex; align-items: center; gap: 7px; line-height: 16px; }
  .contact svg { flex: none; }
  .social { position: absolute; left: 344px; top: 612px; color: var(--white); }
  .social__label { font-size: 12px; margin-bottom: 10px; }
  .social__dots { display: flex; gap: 14px; }
  .social__dots span { width: 14px; height: 14px; border-radius: 50%; background: var(--white); display: block; }

  /* Front cover */
  .front-cover { background: var(--ink); }
  .front-cover__top {
    position: absolute; left: 0; top: 0; width: 100%; height: 320px;
    background: linear-gradient(180deg, #f4f4f4 0%, #dcdcdc 100%);
  }
  .front-cover__top::after {
    content: ""; position: absolute; left: 0; bottom: 0; width: 100%; height: 5px; background: var(--silver);
  }
  .brand { position: absolute; left: 27px; top: 46px; text-align: center; }
  .brand__name {
    border: 1.5px solid var(--ink); padding: 6px 12px;
    font-family: "Oswald", sans-serif; font-weight: 400; font-size: 22px; letter-spacing: 3px; color: var(--ink);
  }
  .brand__url { font-family: "Oswald", sans-serif; font-size: 9.5px; letter-spacing: 2.4px; color: var(--ink); margin-top: 4px; }

  .feature-ring { position: absolute; left: 0; top: 0; }

  .headline { position: absolute; left: 24px; top: 534px; color: var(--white); }
  .headline__lead { font-family: "Archivo Black", sans-serif; font-size: 20px; letter-spacing: .5px; line-height: 24px; }
  .headline__sub { font-family: "Oswald", sans-serif; font-weight: 400; font-size: 19px; color: var(--grey-text); line-height: 26px; }
  .headline__main { font-family: "Oswald", sans-serif; font-weight: 400; font-size: 29px; color: var(--grey-text); line-height: 36px; }
  .headline__call { font-family: "Oswald", sans-serif; font-weight: 300; font-size: 13px; letter-spacing: 5.2px; margin-top: 10px; }
</style>
</head>
<body>
  <div class="spread">
    <section class="page back-cover">
      <div class="back-cover__skyline" role="img" aria-label="Faded grey aerial photograph of a coastal city skyline"></div>
      <div class="back-cover__rule"></div>
      <div class="contact">
        <div class="contact__phone">
          <svg width="11" height="11" viewBox="0 0 24 24"><path fill="#fff" d="M6.6 10.8a15 15 0 0 0 6.6 6.6l2.2-2.2a1 1 0 0 1 1-.25 11 11 0 0 0 3.6.6 1 1 0 0 1 1 1V20a1 1 0 0 1-1 1A17 17 0 0 1 3 4a1 1 0 0 1 1-1h3.5a1 1 0 0 1 1 1c0 1.25.2 2.45.6 3.6a1 1 0 0 1-.25 1z"/></svg>
          0418 293 540
        </div>
        <div class="contact__line">
          <svg width="10" height="10" viewBox="0 0 20 20"><circle cx="10" cy="10" r="8.5" fill="none" stroke="#fff" stroke-width="2"/><path d="M1.5 10h17M10 1.5c-4 4.5-4 12.5 0 17M10 1.5c4 4.5 4 12.5 0 17" fill="none" stroke="#fff" stroke-width="1.6"/></svg>
          www.leasemeridian.com.au
        </div>
        <div class="contact__line">
          <svg width="10" height="8" viewBox="0 0 20 16"><rect x="0" y="0" width="20" height="16" fill="#fff"/><path d="M0 0l10 8 10-8" fill="none" stroke="#0b0b0b" stroke-width="2"/></svg>
          tparks@leasemeridian.com.au
        </div>
      </div>
      <div class="social">
        <div class="social__label">like us</div>
        <div class="social__dots"><span></span><span></span><span></span><span></span></div>
      </div>
    </section>

    <section class="page front-cover">
      <div class="front-cover__top"></div>
      <div class="brand">
        <div class="brand__name">LEASEMERIDIAN</div>
        <div class="brand__url">WWW.LEASEMERIDIAN.COM.AU</div>
      </div>
      <svg class="feature-ring" width="500" height="695" viewBox="0 0 500 695">
        <defs>
          <linearGradient id="city-photo" x1="0" y1="0" x2="0" y2="1">
            <stop offset="0" stop-color="var(--sky-top)"/>
            <stop offset=".4" stop-color="var(--sky-low)"/>
            <stop offset=".6" stop-color="var(--city)"/>
            <stop offset="1" stop-color="#6f675f"/>
          </linearGradient>
        </defs>
        <circle cx="358" cy="309" r="226" fill="var(--ink)"/>
        <circle cx="358" cy="309" r="213" fill="var(--silver)"/>
        <circle cx="358" cy="309" r="205" fill="url(#city-photo)" role="img" aria-label="Photograph of a downtown city skyline at sunset"/>
      </svg>
      <div class="headline">
        <div class="headline__lead">PARKS IS AN INDUSTRY</div>
        <div class="headline__sub">EXPERT WITH A HISTORY OF EXCELLENCE</div>
        <div class="headline__main">IN PROPERTY MANAGEMENT</div>
        <div class="headline__call">CALL TODAY 0418 293 540</div>
      </div>
    </section>
  </div>
</body>
</html>
```